New Look Driving School Project

Current website:
www. kelmorawheelacademy.com

Websites that we like (use content and courses from here as well):
https://www. tollbenroadclass.com

We are looking for a fresh looking driving school website that is easy for students to find the course they are looking for, the price, and allow them to book a lesson all on our website. We would like for this website to have multiple pages: Home, Teen Courses, Adult Courses, About Us, Contact, FAQ, Blog, Requirements.

Target Market(s)

Students in High School or Parents

Industry/Entity Type

Education

Coding

Coded - Design and coding required

Number of Pages Required

5+ page

Font styles to use
Serif
Sans Serif

Colors

Designer to choose colors to be used in the design.

Requirements
Must have
• Must have a form submission and payment processing option. Must have the ability to pick a course, see available times, and process their payment online. MUST BE MOBILE FRIENDLY DESIGN.
Nice to have
• Nice to have a clean format, with big bold fonts.
Should not have
• Should not have a lot of sliders or animations. Should be very fast loading on mobile. Keep it simple but easy to read and elegant.

```html
<!DOCTYPE html>
<html lang="en">
<head>
<meta charset="utf-8">
<title>Kelmora Wheel Academy</title>
<link href="https://fonts.googleapis.com/css2?family=Roboto+Condensed:wght@700&family=Roboto:wght@400;500;700&display=swap" rel="stylesheet">
<style>
:root{
  --stage:#151515;
  --red:#f0174a;
  --blue:#1d55e0;
  --ink:#111111;
  --text:#6b6f78;
  --light:#eef4fd;
  --white:#ffffff;
  --foot:#0b0b0b;
}
*{box-sizing:border-box;margin:0;padding:0}
html,body{width:1200px;height:2960px;overflow:hidden;background:var(--stage);font-family:"Roboto",Arial,sans-serif;color:var(--ink)}
.stage{position:relative;width:1200px;height:2960px;background:var(--stage)}
.band{position:absolute;left:0;top:1337px;width:1200px;height:401px;background:var(--red)}
.h{font-family:"Roboto Condensed","Arial Narrow",sans-serif;font-weight:700;text-transform:uppercase;letter-spacing:.5px}
.abs{position:absolute}
.photo{position:absolute}
/* desktop */
.desk{position:absolute;left:146px;top:225px;width:688px;height:2517px;background:var(--white);overflow:hidden}
.d-head{position:absolute;left:0;top:0;width:688px;height:64px;background:var(--white)}
.d-logo{position:absolute;left:0;top:0;width:234px;height:76px;background:var(--ink);clip-path:polygon(0 0,100% 0,78% 100%,0 100%);border-bottom:5px solid var(--red);z-index:3;display:flex;align-items:center;padding-left:58px;gap:8px}
.logo-dot{width:24px;height:24px;border-radius:50%;background:var(--red);flex:none}
.logo-name{color:var(--white);font-family:"Roboto Condensed",sans-serif;font-weight:700;font-size:14px;line-height:1.05;text-transform:uppercase}
.d-info{position:absolute;top:9px;font-size:6.5px;font-weight:700;line-height:1.2}
.d-info span{display:block;color:var(--text);font-weight:400}
.ring{position:absolute;width:18px;height:18px;border:1.5px solid var(--red);border-radius:50%}
.btn{display:inline-block;font-weight:700;font-size:6.5px;color:var(--white);background:var(--blue);text-transform:uppercase;text-align:center}
.d-nav{position:absolute;left:248px;top:46px;display:flex;gap:13px;font-size:7px;font-weight:700;text-transform:uppercase}
.d-nav .on{color:var(--red)}
.d-rule{position:absolute;left:234px;top:39px;width:454px;height:1px;background:#e3e3e3}
.d-hero{left:0;top:64px;width:688px;height:362px;background:linear-gradient(110deg,#3a3431 0%,#8a6a55 30%,#c8a58a 45%,#6b5a50 65%,#2a2a2c 100%)}
.d-hero-text{position:absolute;left:51px;top:283px;color:var(--white);width:300px}
.d-hero-text h1{font-size:20px;line-height:1}
.d-hero-text p{font-size:8px;line-height:1.6;margin-top:8px}
.form{position:absolute;background:var(--white);box-shadow:0 4px 18px rgba(0,0,0,.12)}
.form h2{font-size:14px}
.form h2 u{text-decoration:none;border-bottom:3px solid var(--red)}
.field{position:absolute;border:1px solid #dde3ec;background:var(--white)}
.field i{position:absolute;left:0;top:0;bottom:0;background:#e9eef7}
.field span{position:absolute;color:#a6adba}
.btn-red{background:var(--red);color:var(--white);font-weight:700;text-transform:uppercase;text-align:center;position:absolute}
.d-feat{position:absolute;left:0;top:426px;width:688px;height:289px;background:var(--light)}
.sec-title{position:absolute;left:0;width:100%;text-align:center}
.feat{position:absolute;width:160px;text-align:center}
.feat svg{display:block;margin:0 auto}
.feat h3{font-size:9px;margin-top:8px;font-family:"Roboto",sans-serif;font-weight:500}
.feat p{font-size:7.5px;color:var(--text);line-height:1.6;margin-top:3px}
.d-about-text{position:absolute;left:370px;top:813px;width:270px}
.d-about-text h2{font-size:19px}
.d-about-text p{font-size:7.5px;color:var(--text);line-height:1.85;margin-top:6px}
.cta{position:absolute;background:linear-gradient(100deg,var(--red),#e3123f 70%,#f42a58);color:var(--white)}
.tabs{position:absolute;width:100%;text-align:center;font-size:6.5px;font-weight:700;text-transform:uppercase}
.tabs b{color:var(--red);margin-right:18px}
.card{position:absolute;background:var(--white);box-shadow:0 4px 14px rgba(0,0,0,.1)}
.card h4{font-size:9.5px;font-family:"Roboto",sans-serif;font-weight:700}
.card p{font-size:7px;color:var(--text);line-height:1.6}
.price{font-size:9.5px;font-weight:500}
.quote{position:absolute;background:linear-gradient(100deg,#4a4a48 0%,#6a5a48 40%,#8a6e52 55%,#3b3b3e 100%)}
.avatar{position:absolute;border-radius:50%;border:3px solid var(--white);background:#bca58d}
.avatar.red{border-color:var(--red)}
.date{position:absolute;background:var(--blue);color:var(--white);text-align:center;font-family:"Roboto Condensed",sans-serif;font-weight:700}
.date.red{background:var(--red)}
.date small{display:block;font-size:5px;letter-spacing:1px}
.more{display:inline-block;background:#e8e8e8;font-weight:700;text-transform:uppercase;color:var(--ink)}
.promo{position:absolute;background:var(--blue);color:var(--white)}
.ghost{position:absolute;border:1.5px solid var(--white);color:var(--white);font-weight:700;text-transform:uppercase;text-align:center}
.foot{position:absolute;background:var(--foot);color:#d8d8d8}
.foot h5{color:var(--white);font-family:"Roboto Condensed",sans-serif;font-weight:700;text-transform:uppercase}
.foot ul{list-style:none}
.input{background:#1c1c1c;color:#777}
.up{position:absolute;border-radius:50%;background:var(--white)}
/* mobile */
.mob{position:absolute;left:890px;top:225px;width:145px;height:2517px;background:var(--white);overflow:hidden}
</style>
</head>
<body>
<div class="stage">
<div class="band"></div>

<!-- DESKTOP -->
<main class="desk">
  <header class="d-head">
    <div class="d-logo"><span class="logo-dot"></span><span class="logo-name">Kelmora Wheel<br>Academy</span></div>
    <div class="d-rule"></div>
    <span class="ring" style="left:347px;top:9px"></span>
    <div class="d-info" style="left:370px">OPENING HOURS<span>MON – FRI 8:00 AM – 7:00 PM</span></div>
    <span class="ring" style="left:482px;top:9px"></span>
    <div class="d-info" style="left:505px">CALL NOW!<span>555-014-2870</span></div>
    <span class="btn" style="position:absolute;left:566px;top:9px;width:71px;height:18px;line-height:18px">Student Login</span>
    <nav class="d-nav"><span class="on">Home</span><span>Teen Courses</span><span>Adult Courses</span><span>About Us</span><span>Contact</span><span>FAQ</span><span>Blog</span><span>Requirements</span></nav>
  </header>
  <div class="photo d-hero" role="img" aria-label="Young woman smiling from the driver's seat of a car"></div>
  <div class="d-hero-text">
    <h1 class="h">We are experts in teen<br>driving education in Fairfax</h1>
    <p>Kelmora Wheel Academy specializes in Behind the Wheel for Teens and Adults, Learners Permits, and Drivers Education.</p>
  </div>

  <div class="d-feat"></div>
  <form class="form" style="left:409px;top:157px;width:228px;height:313px">
    <h2 class="h abs" style="left:28px;top:32px">Find <u>Driving Courses</u></h2>
    <p class="abs" style="left:28px;top:53px;width:175px;font-size:7.5px;color:var(--text);line-height:1.4">Experienced Instructors and Well Maintained Cars/Vehicles.</p>
    <div class="field" style="left:30px;top:84px;width:163px;height:23px"><i style="width:23px"></i><span style="left:31px;top:7px;font-size:6.5px">Enter your name</span></div>
    <div class="field" style="left:30px;top:120px;width:163px;height:23px"><i style="width:23px"></i><span style="left:31px;top:7px;font-size:6.5px">Enter your E-Mail</span></div>
    <div class="field" style="left:30px;top:155px;width:163px;height:23px"><i style="width:23px"></i><span style="left:31px;top:7px;font-size:6.5px">Enter your Phone</span></div>
    <div class="field" style="left:30px;top:191px;width:74px;height:23px"><i style="width:23px"></i><span style="left:31px;top:7px;font-size:6.5px">Car ty… ▾</span></div>
    <div class="field" style="left:119px;top:191px;width:74px;height:23px"><i style="width:23px"></i><span style="left:31px;top:7px;font-size:6.5px">Driving ▾</span></div>
    <div class="field" style="left:30px;top:227px;width:74px;height:23px"><i style="width:23px"></i><span style="left:31px;top:7px;font-size:6.5px">Date</span></div>
    <div class="field" style="left:119px;top:227px;width:74px;height:23px"><i style="width:23px"></i><span style="left:31px;top:7px;font-size:6.5px">Time ▾</span></div>
    <div class="btn-red" style="left:30px;top:263px;width:163px;height:24px;line-height:24px;font-size:7.5px">Find Courses</div>
  </form>

  <h2 class="h sec-title" style="top:510px;font-size:19px">The Best Features</h2>
  <div class="feat" style="left:69px;top:558px">
    <svg width="34" height="38" viewBox="0 0 34 38" fill="none" stroke="#111" stroke-width="1.6"><circle cx="17" cy="11" r="8"/><path d="M3 37c0-9 6-14 14-14s14 5 14 14z"/><path d="M17 23v14" stroke="#f0174a"/></svg>
    <h3>EXPERIENCED INSTRUCTORS</h3><p>Lorem Ipsum is simply dummy text of the printing and typesetting .</p></div>
  <div class="feat" style="left:264px;top:558px">
    <svg width="42" height="38" viewBox="0 0 42 38" fill="none" stroke="#111" stroke-width="1.6"><circle cx="12" cy="8" r="6"/><circle cx="25" cy="8" r="6"/><rect x="2" y="15" width="30" height="21" rx="2"/><path d="M32 22l8-5v17l-8-5" /><path d="M14 20v11l9-5.5z" stroke="#f0174a"/></svg>
    <h3>VIDEO CLASSES</h3><p>Lorem Ipsum is simply dummy text of the printing and typesetting .</p></div>
  <div class="feat" style="left:460px;top:558px">
    <svg width="38" height="38" viewBox="0 0 38 38" fill="none" stroke="#111" stroke-width="1.6"><circle cx="19" cy="19" r="17"/><circle cx="19" cy="19" r="12"/><path d="M19 19l7-6" stroke="#f0174a"/><circle cx="19" cy="25" r="3" stroke="#f0174a"/></svg>
    <h3>BEST SAFETY MEASURES</h3><p>Lorem Ipsum is simply dummy text of the printing and typesetting .</p></div>

  <div class="photo" role="img" aria-label="Smiling instructor and student in the front seats of a car" style="left:51px;top:770px;width:283px;height:187px;background:linear-gradient(100deg,#b9c0c4,#7d7a74 45%,#ddd8d0 100%)"></div>
  <div class="d-about-text">
    <h2 class="h">About Us</h2>
    <p>Lorem Ipsum is simply dummy text of the printing and typesetting industry. Lorem Ipsum has been the industry's standard dummy text ever since the 1500s, when an unknown printer took a galley of type and scrambled it to make a type specimen book. It has survived not only five centuries, but also the leap into .</p>
    <span class="btn" style="margin-top:9px;width:75px;height:19px;line-height:19px">Send Request</span>
  </div>

  <section class="cta" style="left:0;top:1013px;width:688px;height:99px">
    <h2 class="h abs" style="left:51px;top:38px;font-size:19px">Questions about pricing or schedules?</h2>
    <p class="abs" style="left:51px;top:61px;font-size:8px">Call us and we will help you navigate through the process and answer all of your questions!</p>
    <p class="h abs" style="left:501px;top:42px;font-size:15px;text-transform:none">Call: 555-014-2870</p>
  </section>

  <h2 class="h sec-title" style="top:1163px;font-size:19px">Driving Center Courses</h2>
  <div class="tabs" style="top:1191px"><b>Teen Courses</b>Adult Courses</div>
  <div class="card" style="left:51px;top:1218px;width:190px;height:234px">
    <div class="photo" role="img" aria-label="Mature man driving a car" style="left:0;top:0;width:190px;height:137px;background:linear-gradient(120deg,#8c8f93,#4c4f54 50%,#b7b9bb)"></div>
    <h4 class="abs" style="left:13px;top:153px">1 HOUR LESSON PLUS ROAD TEST</h4>
    <p class="abs" style="left:13px;top:168px;width:165px">Lorem Ipsum is simply dummy text of the printing and typesetting industry.</p>
    <span class="price abs" style="left:13px;top:207px">$139.00</span>
    <span class="btn abs" style="left:119px;top:200px;width:70px;height:20px;line-height:20px">Book a Lesson</span>
  </div>
  <div class="card" style="left:249px;top:1218px;width:190px;height:234px">
    <div class="photo" role="img" aria-label="Salesman and customer at a car dealership" style="left:0;top:0;width:190px;height:137px;background:linear-gradient(120deg,#9aa6b4,#3e4a59 45%,#cfd6de)"></div>
    <h4 class="abs" style="left:13px;top:153px">5 DRIVING LESSONS PACKAGE 5 1</h4>
    <p class="abs" style="left:13px;top:168px;width:165px">Lorem Ipsum is simply dummy text of the printing and typesetting industry.</p>
    <span class="price abs" style="left:13px;top:207px">$250.00</span>
    <span class="btn abs" style="left:119px;top:200px;width:70px;height:20px;line-height:20px;background:var(--red)">Book a Lesson</span>
  </div>
  <div class="card" style="left:447px;top:1218px;width:190px;height:234px">
    <div class="photo" role="img" aria-label="Tired driver yawning in a red car" style="left:0;top:0;width:190px;height:137px;background:linear-gradient(120deg,#c13b3b,#7a6a60 45%,#d9cfc4)"></div>
    <h4 class="abs" style="left:13px;top:153px">SILVER PACKAGE 5 1</h4>
    <p class="abs" style="left:13px;top:168px;width:165px">Lorem Ipsum is simply dummy text of the printing and typesetting industry.</p>
    <span class="price abs" style="left:13px;top:207px">$399.00</span>
    <span class="btn abs" style="left:119px;top:200px;width:70px;height:20px;line-height:20px">Book a Lesson</span>
  </div>

  <section class="quote" role="img" aria-label="Car on a road at sunset" style="left:0;top:1511px;width:688px;height:226px"></section>
  <p class="abs" style="left:120px;top:1600px;width:448px;text-align:center;color:var(--white);font-size:11px;font-weight:500;line-height:1.5">Lorem Ipsum is simply dummy text of the printing and typesetting industry lorem Ipsum has been the industry's standard dummy text ever since the 1500s, when an unknown printer .<br><b>Dana Reeves</b></p>
  <span class="avatar" role="img" aria-label="Student portrait" style="left:278px;top:1717px;width:40px;height:40px"></span>
  <span class="avatar red" role="img" aria-label="Student portrait" style="left:324px;top:1717px;width:40px;height:40px"></span>
  <span class="avatar" role="img" aria-label="Student portrait" style="left:370px;top:1717px;width:40px;height:40px"></span>

  <h2 class="h sec-title" style="top:1795px;font-size:19px">Latest Blog</h2>
  <div class="card" style="left:51px;top:1855px;width:180px;height:232px">
    <div class="date" style="left:23px;top:28px;width:32px;height:36px;padding-top:5px;font-size:15px">09<small>APR</small></div>
    <h4 class="h abs" style="left:23px;top:77px;font-size:11px;line-height:1">Nervous drivers are<br>our speciality</h4>
    <p class="abs" style="left:23px;top:105px;font-size:6px;color:var(--ink)">JAN 28,2019 | Admin 24 Comments Driver</p>
    <p class="abs" style="left:23px;top:119px;width:140px">Aenean varius velit lorem, ac rhoncus nisi dictum at. Curabitur rutrum felis eu nunc euismod, sed rutrum magna vestibunean felis eu nunc eu lorem um magna vestibulur ulrper .</p>
    <span class="more abs" style="left:24px;top:183px;width:70px;height:18px;line-height:18px;font-size:6.5px;text-align:center">Read More</span>
  </div>
  <div class="card" style="left:232px;top:1833px;width:224px;height:278px">
    <div class="photo" role="img" aria-label="Couple smiling in the front seats of a car" style="left:0;top:0;width:224px;height:165px;background:linear-gradient(110deg,#6c7d8c,#a58f7c 50%,#cfc5ba);clip-path:polygon(0 0,100% 0,100% 70%,50% 100%,0 70%)"></div>
    <div class="date red" style="left:28px;top:117px;width:30px;height:33px;padding-top:4px;font-size:14px">09<small>APR</small></div>
    <h4 class="h abs" style="left:26px;top:196px;font-size:11px;line-height:1">Nervous drivers are<br>our speciality</h4>
    <p class="abs" style="left:26px;top:224px;font-size:6px;color:var(--ink)">JAN 28,2019 | Admin 24 Comments Driver</p>
    <span class="more abs" style="left:28px;top:242px;width:70px;height:18px;line-height:18px;font-size:6.5px;text-align:center">Read More</span>
  </div>
  <div class="card" style="left:457px;top:1855px;width:180px;height:232px">
    <div class="date" style="left:23px;top:28px;width:32px;height:36px;padding-top:5px;font-size:15px">09<small>APR</small></div>
    <h4 class="h abs" style="left:23px;top:77px;font-size:11px;line-height:1">Nervous drivers are<br>our speciality</h4>
    <p class="abs" style="left:23px;top:105px;font-size:6px;color:var(--ink)">JAN 28,2019 | Admin 24 Comments Driver</p>
    <p class="abs" style="left:23px;top:119px;width:140px">Aenean varius velit lorem, ac rhoncus nisi dictum at. Curabitur rutrum felis eu nunc euismod, sed rutrum magna vestibunean felis eu nunc eu lorem um magna vestibulur ulrper .</p>
    <span class="more abs" style="left:24px;top:183px;width:70px;height:18px;line-height:18px;font-size:6.5px;text-align:center">Read More</span>
  </div>

  <section class="promo" style="left:0;top:2179px;width:688px;height:98px">
    <h2 class="h abs" style="left:50px;top:35px;font-size:23px">Save 10% order now!</h2>
    <p class="abs" style="left:50px;top:62px;font-size:8px">Only this month! Book learning and receive a discount of 10% .....not included packages</p>
    <div class="ghost" style="left:511px;top:42px;width:126px;height:23px;line-height:20px;font-size:8px">Send Request</div>
  </section>

  <footer class="foot" style="left:0;top:2277px;width:688px;height:240px">
    <div class="abs" style="left:51px;top:46px;width:150px"><h5 style="font-size:11px">About</h5><p style="font-size:7px;line-height:1.75;margin-top:5px">Lorem Ipsum is simply dummy text of the printing and typesetting industry. Lorem Ipsum has been the industry's standard dummy text ever since the 1500s, when an unknown printer took a galley of type and scrambled it to make .</p></div>
    <div class="abs" style="left:238px;top:46px"><h5 style="font-size:11px">Links</h5><ul style="font-size:7px;line-height:1.75;margin-top:5px"><li>Home</li><li>Teen Courses</li><li>Adult Courses</li><li>About Us</li><li>Contact</li><li>FAQ</li><li>Blog</li><li>Requirements</li></ul></div>
    <div class="abs" style="left:340px;top:46px"><h5 style="font-size:11px">Newsletter</h5><p style="font-size:7px;margin-top:5px">Subscribe to our newsletter</p>
      <div class="input" style="width:133px;height:20px;line-height:20px;padding-left:10px;font-size:6.5px;margin-top:10px">Email Address</div>
      <div class="btn-red" style="position:static;width:71px;height:20px;line-height:20px;font-size:7px;margin-top:5px">Subscribe</div></div>
    <div class="abs" style="left:516px;top:46px"><h5 style="font-size:11px">Contact Us</h5><ul style="font-size:7px;line-height:1.75;margin-top:5px"><li><b style="color:var(--blue)">●</b> 12 Harrow Lane, Bellmont</li><li><b style="color:var(--blue)">●</b> Phone: (555) 010-4471</li><li><b style="color:var(--blue)">●</b> Fax: (555) 010-4472</li><li><b style="color:var(--blue)">●</b> Email: hello@kelmorawheel.test</li></ul>
      <div style="display:flex;gap:6px;margin-top:8px"><i style="width:7px;height:7px;background:#ddd;border-radius:50%"></i><i style="width:7px;height:7px;background:#ddd;border-radius:50%"></i><i style="width:7px;height:7px;background:#ddd;border-radius:50%"></i><i style="width:7px;height:7px;background:#ddd;border-radius:50%"></i></div></div>
    <div class="up" style="left:626px;top:190px;width:21px;height:21px"><svg width="21" height="21" viewBox="0 0 21 21"><path d="M7 12l3.5-3.5L14 12" fill="none" stroke="#111" stroke-width="1.4"/></svg></div>
    <div class="abs" style="left:51px;top:209px;width:586px;height:1px;background:#2a2a2a"></div>
    <p class="abs" style="left:0;top:220px;width:100%;text-align:center;font-size:7px;color:var(--white)">Copyright 2019 | All Right Reserved</p>
  </footer>
</main>

<!-- MOBILE -->
<main class="mob">
  <header class="abs" style="left:0;top:0;width:145px;height:30px;background:var(--white)">
    <div class="abs" style="left:0;top:0;width:93px;height:30px;background:var(--ink);clip-path:polygon(0 0,100% 0,88% 100%,0 100%);display:flex;align-items:center;gap:4px;padding-left:19px;border-bottom:2px solid var(--red)"><span class="logo-dot" style="width:11px;height:11px"></span><span class="logo-name" style="font-size:6px">Kelmora Wheel<br>Academy</span></div>
    <svg class="abs" style="left:125px;top:11px" width="12" height="9" viewBox="0 0 12 9"><path d="M0 1h12M0 4.5h12M0 8h12" stroke="#111" stroke-width="1.3"/></svg>
  </header>
  <div class="photo" role="img" aria-label="Young woman smiling from the driver's seat of a car" style="left:0;top:30px;width:145px;height:237px;background:linear-gradient(170deg,#6e5a4c,#c09a80 35%,#3a3330 75%,#222)"></div>
  <div class="abs" style="left:7px;top:147px;width:130px;color:var(--white)"><h1 class="h" style="font-size:10px;line-height:1.05">We are experts in teen driving educa-tion in Fairfax</h1><p style="font-size:5.5px;line-height:1.5;margin-top:3px">Kelmora Wheel Academy specializes in Behind the Wheel for Teens and Adults, Learners Permits, and Drivers Education.</p></div>
  <div class="abs" style="left:0;top:267px;width:145px;height:534px;background:var(--light)"></div>
  <form class="form" style="left:6px;top:237px;width:133px;height:213px">
    <h2 class="h abs" style="left:6px;top:17px;font-size:9.5px">Find <u>Driving Courses</u></h2>
    <p class="abs" style="left:6px;top:31px;width:120px;font-size:5px;color:var(--text)">Experienced Instructors and Well Maintained Cars/Vehicles.</p>
    <div class="field" style="left:9px;top:53px;width:115px;height:14px"><i style="width:14px"></i><span style="left:20px;top:3px;font-size:4.5px">Enter your name</span></div>
    <div class="field" style="left:9px;top:78px;width:115px;height:14px"><i style="width:14px"></i><span style="left:20px;top:3px;font-size:4.5px">Enter your E-Mail</span></div>
    <div class="field" style="left:9px;top:104px;width:115px;height:14px"><i style="width:14px"></i><span style="left:20px;top:3px;font-size:4.5px">Enter your Phone</span></div>
    <div class="field" style="left:9px;top:129px;width:53px;height:14px"><i style="width:14px"></i><span style="left:20px;top:3px;font-size:4.5px">Car ty… ▾</span></div>
    <div class="field" style="left:71px;top:129px;width:53px;height:14px"><i style="width:14px"></i><span style="left:20px;top:3px;font-size:4.5px">Driving ▾</span></div>
    <div class="field" style="left:9px;top:154px;width:53px;height:14px"><i style="width:14px"></i><span style="left:20px;top:3px;font-size:4.5px">Date</span></div>
    <div class="field" style="left:71px;top:154px;width:53px;height:14px"><i style="width:14px"></i><span style="left:20px;top:3px;font-size:4.5px">Time ▾</span></div>
    <div class="btn-red" style="left:9px;top:178px;width:115px;height:17px;line-height:17px;font-size:5px">Find Courses</div>
  </form>
  <h2 class="h sec-title" style="top:502px;font-size:11px">The Best Features</h2>
  <div class="feat" style="left:7px;top:526px;width:131px">
    <svg width="26" height="30" viewBox="0 0 34 38" fill="none" stroke="#111" stroke-width="1.6"><circle cx="17" cy="11" r="8"/><path d="M3 37c0-9 6-14 14-14s14 5 14 14z"/><path d="M17 23v14" stroke="#f0174a"/></svg>
    <h3 style="font-size:7px;margin-top:5px">EXPERIENCED INSTRUCTORS</h3><p style="font-size:6px">Lorem Ipsum is simply dummy text of the printing and typesetting .</p></div>
  <div class="feat" style="left:7px;top:609px;width:131px">
    <svg width="34" height="30" viewBox="0 0 42 38" fill="none" stroke="#111" stroke-width="1.6"><circle cx="12" cy="8" r="6"/><circle cx="25" cy="8" r="6"/><rect x="2" y="15" width="30" height="21" rx="2"/><path d="M32 22l8-5v17l-8-5"/><path d="M14 20v11l9-5.5z" stroke="#f0174a"/></svg>
    <h3 style="font-size:7px;margin-top:5px">VIDEO CLASSES</h3><p style="font-size:6px">Lorem Ipsum is simply dummy text of the printing and typesetting .</p></div>
  <div class="feat" style="left:7px;top:694px;width:131px">
    <svg width="30" height="30" viewBox="0 0 38 38" fill="none" stroke="#111" stroke-width="1.6"><circle cx="19" cy="19" r="17"/><circle cx="19" cy="19" r="12"/><path d="M19 19l7-6" stroke="#f0174a"/><circle cx="19" cy="25" r="3" stroke="#f0174a"/></svg>
    <h3 style="font-size:7px;margin-top:5px">BEST SAFETY MEASURES</h3><p style="font-size:6px">Lorem Ipsum is simply dummy text of the printing and typesetting .</p></div>
  <div class="photo" role="img" aria-label="Smiling instructor and student in the front seats of a car" style="left:6px;top:823px;width:133px;height:87px;background:linear-gradient(100deg,#b9c0c4,#7d7a74 45%,#ddd8d0)"></div>
  <div class="abs" style="left:7px;top:925px;width:133px"><h2 class="h" style="font-size:11px">About Us</h2><p style="font-size:5.8px;color:var(--text);line-height:1.7;margin-top:3px">Lorem Ipsum is simply dummy text of the printing and typesetting industry. Lorem Ipsum has been the industry's standard dummy text ever since the 1500s, when an unknown printer took a galley of type and scrambled it to make a type specimen book.</p><span class="btn" style="margin-top:6px;width:66px;height:16px;line-height:16px;font-size:5px">Send Request</span></div>
  <section class="cta" style="left:0;top:1070px;width:145px;height:118px">
    <h2 class="h abs" style="left:7px;top:28px;width:132px;font-size:8px;line-height:1.05">Questions about pricing or schedules?</h2>
    <p class="abs" style="left:7px;top:51px;width:128px;font-size:5.5px;line-height:1.35">Call us and we will help you navigate through the process and answer all of your questions!</p>
    <p class="h abs" style="left:7px;top:86px;font-size:9px;text-transform:none">Call: 555-014-2870</p>
  </section>
  <h2 class="h sec-title" style="top:1215px;font-size:11px;line-height:1">Driving Center<br>Courses</h2>
  <div class="tabs" style="top:1246px;font-size:5px"><b style="margin-right:18px">Teen Courses</b>Adult Courses</div>
  <div class="card" style="left:6px;top:1260px;width:133px;height:165px">
    <div class="photo" role="img" aria-label="Mature man driving a car" style="left:0;top:0;width:133px;height:96px;background:linear-gradient(120deg,#8c8f93,#4c4f54 50%,#b7b9bb)"></div>
    <h4 class="abs" style="left:9px;top:108px;font-size:6px">1 HOUR LESSON PLUS ROAD TEST</h4>
    <p class="abs" style="left:9px;top:118px;width:116px;font-size:4.8px">Lorem Ipsum is simply dummy text of the printing and typesetting industry.</p>
    <span class="price abs" style="left:9px;top:145px;font-size:6px">$139.00</span>
    <span class="btn abs" style="left:84px;top:141px;width:48px;height:13px;line-height:13px;font-size:4.5px">Book a Lesson</span>
  </div>
  <p class="abs" style="left:0;top:1429px;width:145px;text-align:center;color:#bbb;font-size:7px">• • •</p>
  <section class="quote" role="img" aria-label="Car on a road at sunset" style="left:0;top:1458px;width:145px;height:183px"></section>
  <p class="abs" style="left:6px;top:1536px;width:133px;text-align:center;color:var(--white);font-size:6.5px;font-weight:500;line-height:1.5">Lorem Ipsum is simply dummy text of the printing and typesetting industry lorem Ipsum has been the industry's standard<br><b style="font-size:8px">Dana Reeves</b></p>
  <span class="avatar" role="img" aria-label="Student portrait" style="left:11px;top:1621px;width:38px;height:38px"></span>
  <span class="avatar red" role="img" aria-label="Student portrait" style="left:53px;top:1621px;width:38px;height:38px"></span>
  <span class="avatar" role="img" aria-label="Student portrait" style="left:95px;top:1621px;width:38px;height:38px"></span>
  <h2 class="h sec-title" style="top:1675px;font-size:11px">Latest Blog</h2>
  <div class="photo" role="img" aria-label="Couple smiling in the front seats of a car" style="left:6px;top:1705px;width:133px;height:138px;background:linear-gradient(110deg,#6c7d8c,#a58f7c 50%,#cfc5ba);clip-path:polygon(0 0,100% 0,100% 70%,50% 100%,0 70%)"></div>
  <div class="date red" style="left:18px;top:1803px;width:20px;height:22px;padding-top:2px;font-size:9px">09<small style="font-size:4px">APR</small></div>
  <h4 class="h abs" style="left:16px;top:1862px;font-size:8px;line-height:1">Nervous drivers are<br>our speciality</h4>
  <p class="abs" style="left:16px;top:1881px;font-size:4.5px">JAN 28,2019 | Admin 24 Comments Driver</p>
  <span class="more abs" style="left:18px;top:1897px;width:40px;height:12px;line-height:12px;font-size:4.5px;text-align:center">Read More</span>
  <section class="promo" style="left:0;top:1961px;width:145px;height:112px">
    <h2 class="h abs" style="left:5px;top:36px;font-size:10px">Save 10% order now!</h2>
    <p class="abs" style="left:7px;top:50px;width:132px;font-size:5px;line-height:1.3">Only this month! Book learning and receive a discount of 10% .....not included packages</p>
    <div class="ghost" style="left:7px;top:72px;width:131px;height:18px;line-height:15px;font-size:6px">Send Request</div>
  </section>
  <footer class="foot" style="left:0;top:2073px;width:145px;height:444px">
    <div class="abs" style="left:7px;top:27px;width:133px"><h5 style="font-size:8px">About</h5><p style="font-size:5.5px;line-height:1.7;margin-top:3px">Lorem Ipsum is simply dummy text of the printing and typesetting industry. Lorem Ipsum has been the industry's standard dummy text ever since the 1500s, when an unknown printer took a galley of type and scrambled it to make .</p></div>
    <div class="abs" style="left:7px;top:110px"><h5 style="font-size:8px">Links</h5><ul style="font-size:5.5px;line-height:1.95;margin-top:2px"><li>Home</li><li>Teen Courses</li><li>Adult Courses</li><li>About Us</li><li>Contact</li><li>FAQ</li><li>Blog</li><li>Requirements</li></ul></div>
    <div class="abs" style="left:7px;top:220px"><h5 style="font-size:8px">Newsletter</h5><p style="font-size:5.5px;margin-top:2px">Subscribe to our newsletter</p>
      <div class="input" style="width:118px;height:16px;line-height:16px;padding-left:8px;font-size:5px;margin-top:7px">Email Address</div>
      <div class="btn-red" style="position:static;width:64px;height:16px;line-height:16px;font-size:5.5px;margin-top:5px">Subscribe</div></div>
    <div class="abs" style="left:7px;top:306px"><h5 style="font-size:8px">Contact Us</h5><ul style="font-size:5.5px;line-height:1.95;margin-top:3px"><li><b style="color:var(--blue)">●</b> 12 Harrow Lane, Bellmont</li><li><b style="color:var(--blue)">●</b> Phone: (555) 010-4471</li><li><b style="color:var(--blue)">●</b> Fax: (555) 010-4472</li><li><b style="color:var(--blue)">●</b> Email: hello@kelmorawheel.test</li></ul>
      <div style="display:flex;gap:5px;margin-top:5px"><i style="width:5px;height:5px;background:#ddd;border-radius:50%"></i><i style="width:5px;height:5px;background:#ddd;border-radius:50%"></i><i style="width:5px;height:5px;background:#ddd;border-radius:50%"></i><i style="width:5px;height:5px;background:#ddd;border-radius:50%"></i></div></div>
    <div class="up" style="left:63px;top:405px;width:19px;height:19px"><svg width="19" height="19" viewBox="0 0 19 19"><path d="M6 11l3.5-3.5L13 11" fill="none" stroke="#111" stroke-width="1.3"/></svg></div>
    <p class="abs" style="left:0;top:430px;width:100%;text-align:center;font-size:5px;color:var(--white)">Copyright 2019 | All Right Reserved</p>
  </footer>
</main>
</div>
</body>
</html>
```